Architectural Design practice needs new logo /letterhead design

We need a new logo / letterhead design to freshen up the practice image. We are an architects practice working in all building design sectors and want a new modern fresh logo / letterhead but retaining a professional feel, so not too gimmicky. The current branding colour palette uses blue and grey, which we still like, but we are also open to other suggestions. I have attached our current letterhead which has served us well and incorporates the FENC logo, but this was produced in-house using only Word when we first started the business and we would now like a new more modern and professional design.
Possibly include the acronym KPT , or kpt, second file added shows an attempt I did myself, which is a bit basic but gives an idea of the type of thing we are looking for

File added showing the type of thing we are looking for

Building

Sans Serif

```html
<!DOCTYPE html>
<html lang="en">
<head>
<meta charset="utf-8">
<title>Kerr Price Talbot – Letterhead</title>
<link href="https://fonts.googleapis.com/css2?family=Poppins:wght@300&display=swap" rel="stylesheet">
<style>
  :root {
    --paper: #ffffff;
    --navy: #1a3668;
    --ink-grey: #8c8c8c;
    --arc-top: #e2e3e5;
    --arc-bottom: #ffffff;
  }
  html, body {
    margin: 0;
    padding: 0;
    overflow: hidden;
    background: var(--paper);
  }
  .letterhead {
    position: relative;
    width: 900px;
    height: 1200px;
    overflow: hidden;
    background: var(--paper);
    font-family: "Poppins", "Century Gothic", sans-serif;
    font-weight: 300;
  }
  .brand {
    position: absolute;
    left: 100px;
    top: 168px;
    width: 215px;
    display: flex;
    align-items: center;
    justify-content: center;
    gap: 8px;
    color: var(--navy);
  }
  .brand-mark {
    width: 14px;
    height: 14px;
    background: var(--navy);
    flex: none;
  }
  .brand-name {
    margin: 0;
    font-size: 20px;
    line-height: 1;
    white-space: nowrap;
  }
  .contact {
    position: absolute;
    left: 340px;
    top: 125px;
    width: 480px;
    text-align: center;
    color: var(--ink-grey);
    font-size: 16px;
    line-height: 18px;
  }
  .contact p { margin: 0; }
  .contact .address { margin-bottom: 14px; }
  .contact .gap { display: inline-block; width: 18px; }
  .footer-arc {
    position: absolute;
    left: 0;
    top: 1040px;
    width: 900px;
    height: 160px;
  }
  .company-details {
    position: absolute;
    left: 0;
    top: 1112px;
    width: 900px;
    text-align: center;
    color: var(--ink-grey);
    font-size: 16.5px;
    line-height: 22.5px;
  }
  .company-details p { margin: 0; }
</style>
</head>
<body>
<div class="letterhead">
  <div class="brand">
    <span class="brand-mark" aria-hidden="true"></span>
    <p class="brand-name">Kerr Price Talbot</p>
  </div>

  <div class="contact">
    <p class="address">Kerr Price Talbot Ltd, Elmfield House,<br>14 Marlow Road, Stafford, Staffs, ST9 4QX</p>
    <p>T 01632 960418<span class="gap"></span>F 01632 960419</p>
    <p>E hello@kerrpricetalbot.co.uk</p>
  </div>

  <svg class="footer-arc" viewBox="0 0 900 160" preserveAspectRatio="none" aria-hidden="true">
    <defs>
      <linearGradient id="arcFill" x1="0" y1="0" x2="0" y2="1">
        <stop offset="0" style="stop-color: var(--arc-top)"/>
        <stop offset="1" style="stop-color: var(--arc-bottom)"/>
      </linearGradient>
    </defs>
    <path d="M0 77 Q450 -63 900 77 L900 160 L0 160 Z" fill="url(#arcFill)"/>
  </svg>

  <div class="company-details">
    <p>Directors: Keith Price BA (Hons) Dip Arch FENC, Laura Talbot</p>
    <p>Registered Office: 22 Ashby Lane, Stafford, Staffs, ST9 2LP.</p>
    <p>Registered in England No. 4817265. VAT No. 914 2207 51</p>
  </div>
</div>
</body>
</html>
```